nonprofit organization looking for sleek new design

We need a fresh new look for this nonprofit organization, Harbor Lights Family Works, INC (HALIF, Inc.). This organization provides educational, nutritional, dental health, and specialized services to Tidewell children, aiming to support families meeting federal income poverty guidelines. Our mission is clear: "Creating a brighter future for the children and la familia." We focus on child development, family wellness, staff growth, and community partnerships.

```html
<!DOCTYPE html>
<html lang="en">
<head>
<meta charset="utf-8">
<title>HALIF, Inc. — Harbor Lights Family Works</title>
<link rel="stylesheet" href="https://fonts.googleapis.com/css2?family=Domine:wght@400;600;700&family=Jost:wght@400;500;600&display=swap">
<style>
:root{
  --hero-blue:#27b3d9;
  --blue:#1a9fd0;
  --deep-blue:#137fa9;
  --navy:#0f6f98;
  --orange:#ff8a00;
  --orange-light:#ffa21a;
  --orange-deep:#ff7300;
  --text:#2b2b2b;
  --muted:#555;
  --line:#b9d6e3;
  --footer-bar:#e6e8ea;
  --white:#fff;
}
*{margin:0;padding:0;box-sizing:border-box}
html,body{width:1200px;height:4769px;overflow:hidden}
body{position:relative;background:var(--white);font-family:"Jost",sans-serif;color:var(--text)}
.abs{position:absolute}
.serif{font-family:"Domine",serif}
.btn{position:absolute;display:flex;align-items:center;justify-content:center;border-radius:30px;font-family:"Jost",sans-serif;font-weight:600;font-size:15px;letter-spacing:.5px;color:var(--white);text-transform:uppercase}
.btn-orange{background:linear-gradient(90deg,var(--orange-deep),var(--orange-light))}
.btn-blue{background:var(--blue)}
.btn-ghost{border:2px solid var(--white)}
.btn .chev{margin-left:8px;font-size:14px}

/* header + hero */
.hero-bg{left:0;top:0;width:1200px;height:700px}
.logo{font-family:"Domine",serif;font-weight:700;font-size:26px;color:var(--white)}
.nav{left:378px;top:32px;display:flex;gap:44px;font-size:13px;font-weight:500;letter-spacing:.6px;color:var(--white)}
.nav-cta{left:954px;top:24px;width:132px;height:36px;font-size:13px}
.hero-title{left:109px;top:205px;width:560px;font-family:"Domine",serif;font-weight:600;font-size:46px;line-height:54px;color:var(--white)}
.hero-title .mark{background:var(--orange);border-radius:6px 26px 8px 22px;padding:0 10px}
.hero-lead{left:109px;top:384px;width:440px;font-size:17px;line-height:28px;color:var(--white)}
.dots{left:32px;top:312px;display:flex;flex-direction:column;gap:12px}
.dots span{width:11px;height:11px;border-radius:50%;border:2px solid var(--white)}
.dots span.on{background:var(--white)}
.hero-photo{left:660px;top:60px;width:540px;height:620px;border-radius:240px 240px 0 0;background:radial-gradient(circle at 45% 35%,#8fd4e9,#2aa9d0 70%)}
.scroll-down{left:568px;top:618px;width:60px;height:60px;border-radius:50%;background:var(--white);border:2px solid #d5eef6;display:flex;align-items:center;justify-content:center}

/* mission */
.mission-box{left:159px;top:791px;width:882px;height:252px;border:1.5px solid var(--line)}
.mission-title{left:0;width:1200px;top:766px;text-align:center;font-family:"Domine",serif;font-size:46px;color:var(--deep-blue)}
.mission-title span{display:inline-block;background:var(--white);padding:0 16px}
.mission-title .brush{background:var(--blue);color:var(--white);border-radius:24px 40px 18px 30px;padding:0 14px}
.mission-sub{left:0;width:1200px;top:856px;text-align:center;font-size:21px;color:var(--text)}
.mission-text{left:215px;top:906px;width:770px;text-align:center;font-size:15.5px;line-height:22px;color:var(--muted)}

/* services */
.services-bg{left:0;top:1156px;width:1200px;height:680px}
.section-title{left:0;width:1200px;text-align:center;font-family:"Domine",serif;font-weight:600}
.underline{position:absolute;height:6px;border-radius:6px}
.card{position:absolute;top:1307px;width:311px;height:373px;background:var(--white);text-align:center}
.card .photo{width:100%;height:193px}
.card .hex{position:absolute;left:118px;top:160px;width:75px;height:80px}
.card h3{margin-top:54px;font-family:"Domine",serif;font-weight:400;font-size:25px;color:var(--text)}
.card p{margin:10px auto 0;width:262px;font-size:13.5px;line-height:22px;color:var(--muted)}
.card.active{background:var(--blue);height:408px;border:2px solid #8ed8ef}
.card.active h3,.card.active p{color:var(--white)}
.card .card-btn{left:86px;top:358px;width:140px;height:32px;font-size:11px}

/* focus */
.focus-title{top:1856px;font-size:44px;color:var(--deep-blue)}
.focus-photo{position:absolute;border-radius:50%}
.ring{position:absolute;border-radius:50%;border:8px solid transparent}
.focus-h{position:absolute;font-family:"Domine",serif;font-weight:600;font-size:37px;color:var(--deep-blue)}
.focus-p{position:absolute;width:490px;font-size:17.5px;line-height:28px;color:var(--text)}
.focus-btn{width:195px;height:50px}

/* cta */
.cta-bg{left:0;top:3660px;width:1200px;height:740px}
.cta-photo{left:0;top:3740px;width:720px;height:653px;background:linear-gradient(90deg,#e8b58e 0%,#d98c4e 40%,#4aa9cf 85%,rgba(31,160,210,0))}
.cta-title{left:648px;top:3920px;width:460px;font-family:"Domine",serif;font-weight:600;font-size:42px;line-height:50px;color:var(--white)}
.cta-title .mark{background:var(--orange);border-radius:8px 28px 10px 24px;padding:0 8px}
.field{position:absolute;background:var(--white);border:1px solid #cfe3ec;font-size:12px;color:#666;padding:13px 18px}
.send{left:654px;top:4254px;width:192px;height:50px}

/* footer */
.foot-logo{left:137px;top:4480px;font-family:"Domine",serif;font-weight:700;font-size:24px;color:var(--deep-blue)}
.foot-about{left:139px;top:4530px;width:260px;font-size:15px;line-height:25px;color:var(--text)}
.foot-col{position:absolute;top:4458px}
.foot-col h4{font-family:"Jost",sans-serif;font-weight:500;font-size:21px;color:var(--deep-blue)}
.foot-col .bar{width:64px;height:4px;background:var(--blue);border-radius:4px;margin:6px 0 14px}
.foot-col li{list-style:none;font-size:15px;line-height:25.5px;color:var(--text)}
.social li{display:flex;align-items:center;gap:10px;line-height:36px}
.social .dot{width:26px;height:26px;border-radius:50%;border:2px solid var(--orange)}
.copyright{left:0;top:4704px;width:1200px;height:65px;background:var(--footer-bar);display:flex;align-items:center;justify-content:center;font-size:13px;color:#444}
</style>
</head>
<body>

<!-- hero -->
<svg class="abs hero-bg" viewBox="0 0 1200 700" aria-hidden="true">
  <defs><linearGradient id="heroGrad" x1="0" x2="1"><stop offset="0" stop-color="#1ea6d4"/><stop offset="1" stop-color="#2fbfe0"/></linearGradient></defs>
  <path d="M0 0H1200V600C1080 660 960 690 800 690C560 690 420 600 240 610C120 615 50 650 0 680Z" fill="url(#heroGrad)"/>
</svg>
<div class="abs hero-photo" role="img" aria-label="Smiling boy carrying a stack of books, surrounded by chalk-style school doodles"></div>
<div class="abs logo" style="left:126px;top:26px">HALIF, Inc.</div>
<nav class="abs nav"><span>ABOUT US</span><span>SERVICES</span><span>PROGRAMS</span><span>BLOGS</span><span>COMMUNITY</span></nav>
<div class="btn btn-orange nav-cta">Contact Us</div>
<div class="abs dots"><span></span><span class="on"></span><span></span></div>
<h1 class="abs hero-title">Creating a brighter future for the <span class="mark">children</span> and la familia.</h1>
<p class="abs hero-lead">Lorem ipsum dolor sit amet, consectetur adipiscing elit, sed do eiusmod tempor incididunt ut</p>
<div class="btn btn-orange" style="left:109px;top:460px;width:173px;height:44px">Contact Us</div>
<div class="btn btn-ghost" style="left:291px;top:460px;width:178px;height:44px">Learn More</div>
<div class="abs scroll-down"><svg width="24" height="24" viewBox="0 0 24 24"><path d="M12 3V20M5 13L12 20L19 13" stroke="#1a9fd0" stroke-width="2" fill="none" stroke-linecap="round"/></svg></div>

<!-- mission -->
<div class="abs mission-box"></div>
<h2 class="abs mission-title"><span>Our <span class="brush">Mission</span></span></h2>
<p class="abs mission-sub">Creating a brighter future for the children and la familia.</p>
<p class="abs mission-text">Lorem ipsum dolor sit amet, consectetur adipiscing elit, sed do eiusmod tempor incididunt ut labore et dolore magna aliqua. Ut enim ad minim veniam, quis nostrud exercitation ullamco laboris nisi ut aliquip ex ea commodo consequat. Duis aute irure dolor in reprehenderit in voluptate</p>
<div class="btn btn-blue" style="left:506px;top:1017px;width:194px;height:48px">Learn More <span class="chev">›</span></div>

<!-- services -->
<svg class="abs services-bg" viewBox="0 0 1200 680" aria-hidden="true">
  <defs><linearGradient id="svcGrad" x1="0" x2="1"><stop offset="0" stop-color="#ff9c0a"/><stop offset="1" stop-color="#ff7600"/></linearGradient></defs>
  <path d="M0 0H1200V640C1100 600 980 590 860 620C700 660 560 690 380 660C220 632 100 600 0 620Z" fill="url(#svcGrad)"/>
</svg>
<h2 class="abs section-title" style="top:1200px;font-size:40px;color:#fff">Services Provide</h2>
<div class="underline" style="left:516px;top:1262px;width:168px;background:#fff"></div>

<div class="card" style="left:117px">
  <div class="photo" role="img" aria-label="Fresh vegetables being prepared on a kitchen counter" style="background:linear-gradient(135deg,#e9e4dc,#c9a27a 55%,#8aa84f)"></div>
  <svg class="hex" viewBox="0 0 75 80"><path d="M37.5 3L71 21V59L37.5 77L4 59V21Z" fill="#1a9fd0" stroke="#fff" stroke-width="4"/><circle cx="37.5" cy="42" r="13" fill="none" stroke="#fff" stroke-width="2.5"/></svg>
  <h3>Nutritional</h3>
  <p>Lorem ipsum dolor sit amet, consectetur adipiscing elit, sed do eiusmod tempor incididunt ut labore et dolore</p>
</div>
<div class="card active" style="left:450px">
  <div class="photo" role="img" aria-label="Teacher standing in front of a classroom of children" style="background:linear-gradient(135deg,#5e6c5a,#c9a64a 50%,#3d4d44)"></div>
  <svg class="hex" viewBox="0 0 75 80"><path d="M37.5 3L71 21V59L37.5 77L4 59V21Z" fill="#fff" stroke="#1a9fd0" stroke-width="3"/><path d="M20 38L37.5 30L55 38L37.5 46Z M27 42V50C32 54 43 54 48 50V42" fill="none" stroke="#1a9fd0" stroke-width="2.5"/></svg>
  <h3>Education Service</h3>
  <p>Lorem ipsum dolor sit amet, consectetur adipiscing elit, sed do eiusmod tempor incididunt ut labore et dolore</p>
  <div class="btn btn-orange card-btn">Learn More <span class="chev">›</span></div>
</div>
<div class="card" style="left:782px">
  <div class="photo" role="img" aria-label="Family sitting together in a bright living room" style="background:linear-gradient(135deg,#d9dcde,#9c8f84 55%,#5d6e7a)"></div>
  <svg class="hex" viewBox="0 0 75 80"><path d="M37.5 3L71 21V59L37.5 77L4 59V21Z" fill="#ff9a14" stroke="#fff" stroke-width="4"/><circle cx="37.5" cy="34" r="6" fill="none" stroke="#fff" stroke-width="2.5"/><path d="M24 54C26 44 49 44 51 54" fill="none" stroke="#fff" stroke-width="2.5"/></svg>
  <h3>Specialized services</h3>
  <p>Lorem ipsum dolor sit amet, consectetur adipiscing elit, sed do eiusmod tempor incididunt ut labore et dolore</p>
</div>

<!-- focus -->
<h2 class="abs section-title focus-title">We Focus on</h2>
<div class="underline" style="left:522px;top:1924px;width:170px;background:var(--blue)"></div>

<svg class="abs" style="left:0;top:2300px" width="1200" height="1120" viewBox="0 0 1200 1120" aria-hidden="true" fill="none" stroke="#1a9fd0" stroke-width="2.5" stroke-dasharray="2 6" stroke-linecap="round">
  <path d="M524 14C540 80 600 70 660 90C700 105 710 130 712 150"/>
  <path d="M700 475C690 540 620 530 570 555C530 575 515 600 515 620"/>
  <path d="M522 1000C540 1050 600 1050 660 1060C690 1070 700 1095 706 1115"/>
</svg>

<!-- child development -->
<div class="ring" style="left:148px;top:1967px;width:400px;height:400px;border-top-color:var(--orange);border-left-color:var(--orange);border-right-color:var(--orange-light);transform:rotate(-20deg)"></div>
<div class="focus-photo" role="img" aria-label="Mother and young daughter doing an activity together" style="left:163px;top:1982px;width:370px;height:370px;background:radial-gradient(circle at 45% 40%,#e6c9b6,#b9876e 60%,#f0ece8)"></div>
<h3 class="focus-h" style="left:600px;top:2026px">Child development</h3>
<p class="focus-p" style="left:605px;top:2093px">Lorem ipsum dolor sit amet, consectetur adipiscing elit, sed do eiusmod tempor incididunt ut labore et dolore magna aliqua. Ut enim ad minim veniam, quis nostrud exercitation ullamco laboris nisi ut aliquip ex ea commodo consequat. Duis aute irure dolor in reprehenderit in voluptate</p>
<div class="btn btn-orange focus-btn" style="left:600px;top:2263px">Learn More <span class="chev">›</span></div>

<!-- family wellness -->
<div class="ring" style="left:689px;top:2402px;width:400px;height:400px;border-top-color:var(--deep-blue);border-right-color:var(--deep-blue);transform:rotate(-10deg)"></div>
<div class="focus-photo" role="img" aria-label="Happy family of three with arms raised outdoors in a park" style="left:709px;top:2422px;width:362px;height:362px;background:radial-gradient(circle at 50% 45%,#d9b79a,#6f9a58 60%,#3f6b3a)"></div>
<h3 class="focus-h" style="left:148px;top:2476px">Family Wellness</h3>
<p class="focus-p" style="left:153px;top:2542px">Lorem ipsum dolor sit amet, consectetur adipiscing elit, sed do eiusmod tempor incididunt ut labore et dolore magna aliqua. Ut enim ad minim veniam, quis nostrud exercitation ullamco laboris nisi ut aliquip ex ea commodo consequat. Duis aute irure dolor in reprehenderit in voluptate</p>
<div class="btn btn-orange focus-btn" style="left:148px;top:2711px">Learn More <span class="chev">›</span></div>

<!-- staff growth -->
<div class="ring" style="left:124px;top:2865px;width:400px;height:400px;border-top-color:#f2b51a;border-left-color:#f2b51a;transform:rotate(-15deg)"></div>
<div class="focus-photo" role="img" aria-label="Colleagues working together around a laptop in an office" style="left:144px;top:2885px;width:360px;height:360px;background:radial-gradient(circle at 50% 45%,#c9b8a8,#6c7f8f 60%,#e9eef2)"></div>
<h3 class="focus-h" style="left:596px;top:2930px">Staff Growth</h3>
<p class="focus-p" style="left:601px;top:2997px">Lorem ipsum dolor sit amet, consectetur adipiscing elit, sed do eiusmod tempor incididunt ut labore et dolore magna aliqua. Ut enim ad minim veniam, quis nostrud exercitation ullamco laboris nisi ut aliquip ex ea commodo consequat. Duis aute irure dolor in reprehenderit in voluptate</p>
<div class="btn btn-orange focus-btn" style="left:596px;top:3167px">Learn More <span class="chev">›</span></div>

<!-- community partnerships -->
<div class="ring" style="left:698px;top:3319px;width:400px;height:400px;border-top-color:var(--navy);border-left-color:var(--navy);transform:rotate(-10deg)"></div>
<div class="focus-photo" role="img" aria-label="Group of people stacking their hands together" style="left:718px;top:3339px;width:362px;height:362px;background:radial-gradient(circle at 50% 55%,#c98a66,#8a5a45 55%,#5c6b78)"></div>
<h3 class="focus-h" style="left:159px;top:3380px">Community partnerships</h3>
<p class="focus-p" style="left:164px;top:3446px">Lorem ipsum dolor sit amet, consectetur adipiscing elit, sed do eiusmod tempor incididunt ut labore et dolore magna aliqua. Ut enim ad minim veniam, quis nostrud exercitation ullamco laboris nisi ut aliquip ex ea commodo</p>
<div class="btn btn-orange focus-btn" style="left:165px;top:3585px">Learn More <span class="chev">›</span></div>

<!-- call to action -->
<svg class="abs cta-bg" viewBox="0 0 1200 740" aria-hidden="true">
  <defs><linearGradient id="ctaGrad" x1="0" x2="1"><stop offset="0" stop-color="#2aaed8"/><stop offset="1" stop-color="#159bcf"/></linearGradient></defs>
  <path d="M0 25C120 60 230 90 380 90C600 90 820 40 1000 60C1080 68 1150 80 1200 70V733H0Z" fill="#7ed0ea"/>
  <path d="M0 95C200 125 360 140 560 125C760 110 960 60 1200 75V733H0Z" fill="url(#ctaGrad)"/>
</svg>
<div class="abs cta-photo" role="img" aria-label="Mother and daughter smiling while drawing in a notebook together"></div>
<h2 class="abs cta-title">Start Building Your Child Bright <span class="mark">Future</span></h2>
<div class="underline" style="left:650px;top:4030px;width:150px;background:#fff"></div>
<div class="field" style="left:650px;top:4050px;width:213px;height:41px">First Name</div>
<div class="field" style="left:870px;top:4050px;width:213px;height:41px">Last Name</div>
<div class="field" style="left:650px;top:4100px;width:213px;height:43px">Email address</div>
<div class="field" style="left:870px;top:4100px;width:213px;height:43px">Phone</div>
<div class="field" style="left:650px;top:4150px;width:433px;height:85px">Message</div>
<div class="btn btn-orange send">Send Message <span class="chev">›</span></div>

<!-- footer -->
<div class="abs foot-logo">HALIF, Inc.</div>
<p class="abs foot-about">Lorem ipsum dolor sit amet, consectetur adipiscing elit, sed do eiusmod tempor incididunt ut</p>
<div class="foot-col" style="left:463px">
  <h4>Quick Links</h4><div class="bar"></div>
  <ul><li>Home</li><li>About Us</li><li>Services</li><li>Our Community</li></ul>
</div>
<div class="foot-col" style="left:684px">
  <h4>Resources</h4><div class="bar"></div>
  <ul><li>Blogs</li><li>Contact Us</li><li>Mission</li><li>Support</li></ul>
</div>
<div class="foot-col social" style="left:909px">
  <h4>Follow Us</h4><div class="bar"></div>
  <ul style="margin-top:-8px"><li><span class="dot"></span>Circlefeed</li><li><span class="dot"></span>Chirpline</li><li><span class="dot"></span>Snapframe</li></ul>
</div>
<div class="abs copyright">© 2023 HALIF, Inc All Rights Reserved</div>

</body>
</html>
```